Zielgruppe
Tobias Fink Personal Training.
Personaltraining für Bürotätige / leitende Positionen.
Rücken- und Haltungstraining.
Zielgruppe: Herren mittleren Alters, gehobene Klasse.
Aufgabenstellung
Schlicht, elegant, hochwertig
Gerne Logo eingearbeitet.
Schwarz / Gold / Weiß

```html
<!DOCTYPE html>
<html lang="de">
<head>
<meta charset="utf-8">
<title>TFPT Visitenkarten</title>
<link rel="stylesheet" href="https://fonts.googleapis.com/css2?family=Open+Sans:wght@400;600&display=swap">
<style>
  :root {
    --stage: #c9c8c8;
    --charcoal: #333333;
    --gold: #c19a2a;
    --paper: #ffffff;
    --ink: #3a3a3a;
    --muted: #7a7a7a;
    --light-text: #d9d9d9;
  }
  * { margin: 0; padding: 0; box-sizing: border-box; }
  html, body { width: 1200px; height: 900px; overflow: hidden; }
  body {
    background: var(--stage);
    font-family: "Open Sans", Arial, sans-serif;
    position: relative;
  }
  .card {
    position: absolute;
    width: 540px;
    height: 350px;
    overflow: hidden;
    box-shadow: 0 6px 18px rgba(0,0,0,0.18);
  }
  .gold-rule { position: absolute; height: 2px; background: var(--gold); }

  /* Brand name placeholder: one colour, one weight, one plain square */
  .brand {
    position: absolute;
    display: flex;
    align-items: center;
    white-space: nowrap;
    color: var(--gold);
    font-weight: 600;
  }
  .brand__mark { flex: none; background: var(--gold); }

  /* Front card */
  .card--front { left: 620px; top: 110px; background: var(--charcoal); }
  .card--front .gold-rule--left { left: 0; top: 150px; width: 150px; }
  .card--front .gold-rule--right { left: 330px; top: 232px; width: 210px; }
  .card--front .brand { left: 165px; top: 136px; font-size: 21px; gap: 10px; }
  .card--front .brand__mark { width: 12px; height: 12px; }

  /* Back card */
  .card--back { left: 40px; top: 440px; background: var(--paper); }
  .person { position: absolute; left: 44px; top: 44px; color: var(--muted); }
  .person__name { font-size: 15px; font-weight: 600; }
  .person__role { font-size: 12px; }
  .divider-vertical {
    position: absolute; left: 262px; top: 92px; width: 2px; height: 140px; background: var(--gold);
  }
  .contact { position: absolute; left: 284px; top: 92px; color: var(--ink); font-size: 15px; line-height: 22px; }
  .contact__company { margin-bottom: 2px; }
  .contact__row { display: flex; align-items: center; gap: 8px; }
  .contact__row svg { width: 14px; height: 14px; flex: none; }
  .contact__address { margin-bottom: 6px; }
  .card--back .gold-rule--bottom { left: 0; top: 282px; width: 200px; }
  .card--back .gold-rule--bottom-right { left: 420px; top: 282px; width: 120px; }
  .band { position: absolute; background: var(--charcoal); height: 34px; }
  .band--left { left: 0; top: 292px; width: 200px; }
  .band--right { left: 420px; top: 300px; width: 120px; }
  .web { position: absolute; left: 18px; top: 301px; font-size: 12px; color: var(--light-text); }
  .card--back .brand { left: 212px; top: 300px; font-size: 11px; gap: 6px; }
  .card--back .brand__mark { width: 7px; height: 7px; }
</style>
</head>
<body>

<section class="card card--front" aria-label="Vorderseite">
  <div class="gold-rule gold-rule--left"></div>
  <div class="brand">
    <span class="brand__mark"></span>
    <span class="brand__name">Tobias Fink Personal Training</span>
  </div>
  <div class="gold-rule gold-rule--right"></div>
</section>

<section class="card card--back" aria-label="Rückseite">
  <div class="person">
    <div class="person__name">Lukas Brenner</div>
    <div class="person__role">Geschäftsführer</div>
  </div>

  <div class="divider-vertical"></div>

  <div class="contact">
    <div class="contact__company">TFPT Ltd</div>
    <div>Lindenweg 18</div>
    <div class="contact__address">A-4120 Birkental</div>
    <div class="contact__row">
      <svg viewBox="0 0 16 16" aria-hidden="true"><path fill="#c19a2a" d="M3.5 1.5l2.5 3-1.5 1.5c.8 1.8 2.2 3.2 4 4l1.5-1.5 3 2.5-1.5 2.5C6.5 13 3 9.5 1 4z"/></svg>
      <span>01234/567 80-10</span>
    </div>
    <div class="contact__row">
      <svg viewBox="0 0 16 16" aria-hidden="true"><rect x="4" y="1" width="8" height="5" fill="#c19a2a"/><rect x="1" y="6" width="14" height="6" rx="1" fill="#c19a2a"/><rect x="4" y="10" width="8" height="5" fill="#fff" stroke="#c19a2a" stroke-width="1.5"/></svg>
      <span>01234/567 80-20</span>
    </div>
    <div class="contact__row">
      <svg viewBox="0 0 16 16" aria-hidden="true"><rect x="1" y="3" width="14" height="10" fill="#c19a2a"/><path d="M1 3l7 6 7-6" fill="none" stroke="#fff" stroke-width="1.4"/></svg>
      <span>info@tfpt-training.de</span>
    </div>
  </div>

  <div class="gold-rule gold-rule--bottom"></div>
  <div class="band band--left"></div>
  <div class="web">www.tfpt-training.de</div>
  <div class="brand">
    <span class="brand__mark"></span>
    <span class="brand__name">Tobias Fink Personal Training</span>
  </div>
  <div class="gold-rule gold-rule--bottom-right"></div>
  <div class="band band--right"></div>
</section>

</body>
</html>
```